New Business Card Design Project

We need to enhance the look and feel of our brand. We are starting with the business card and will hopefully expand to letter head, website, etc. The firm is based in Marholt Nordavia and invests with global pension funds and for mutual fund investors alike. We would like to see an innovative use of the companies logo (star on the website - www.northmerrowcap.com) and a broader use of a color palette. Presently it is dominantly shades of blue. The firm wants to convey a sense they are a creative investment team that understands all the risks in the emerging markets and have the skills to perform in an environment of uncertainty.

Presently, we have three locations: Marholt Nordavia, Glendale CA USA, Zurich Switzerland. We also have a prominently displayed bar code square on a solid dark blue back that will take smart phone users to the firm's website. I am indifferent to its inclusion., Details for my new Business Card Design Project will be added soon.
Updates

Project Deadline Extended
Reason: Designers, I am working with on getting feedback from both US and Danish partners on preferences. That is taking slightly more time than expected. Thanks for you patience. Nice work. TLV

Target Market(s)

The target market is a combination of institutional and retail investors. The european arm uses a card similar to a couple of those submitted.

Industry/Entity Type

Environment

Requirements
Must have
• The company's Star Logo. See www.northmerrowcap.com. It may be used in its current form or some new clever way. The founders are Danish and have a strong affinity for it.
Nice to have
• The new materials may be solely used in the north America and distributed in Australia as well. Therefore, we may try something new in these markets. I'd prefer to see a broader use of the color spectrum, not simply blue.
Should not have
• The card should not look and feel like a bank, insurance company, or a traditional money manager.

```html
<!DOCTYPE html>
<html lang="en">
<head>
<meta charset="utf-8">
<title>Northmerrow Capital – Business Card</title>
<link href="https://fonts.googleapis.com/css2?family=Arimo:wght@400;700&display=swap" rel="stylesheet">
<style>
  :root {
    --page-bg: #ffffff;
    --navy: #043380;
    --navy-deep: #022a6b;
    --cyan: #45dcf3;
    --white: #ffffff;
    --card-shadow: rgba(0, 0, 0, 0.35);
  }
  * { box-sizing: border-box; margin: 0; padding: 0; }
  html, body {
    width: 1200px; height: 1000px; overflow: hidden;
    background: var(--page-bg);
    font-family: "Arimo", Arial, sans-serif;
  }
  .stage {
    position: relative; width: 1200px; height: 1000px;
  }
  .card {
    position: absolute; top: 357px;
    width: 500px; height: 286px;
    overflow: hidden;
    box-shadow: 6px 6px 6px var(--card-shadow);
  }
  .card--front {
    left: 70px;
    background: var(--white);
    border: 3px solid var(--navy);
    text-align: center;
  }
  .brand-dot {
    position: absolute; left: 50%; top: 70px;
    width: 64px; height: 64px; margin-left: -32px;
    border-radius: 50%;
    background: var(--navy);
    border: 4px solid var(--cyan);
  }
  .brand-name {
    position: absolute; left: 0; right: 0; top: 144px;
    font-size: 46px; font-weight: 400; color: var(--cyan);
    letter-spacing: 0.5px; white-space: nowrap;
  }
  .brand-url {
    position: absolute; left: 0; right: 0; top: 200px;
    font-size: 19px; color: var(--navy);
  }
  .card--back {
    left: 630px;
    background: var(--navy);
    color: var(--cyan);
  }
  .back-disc {
    position: absolute; right: 40px; top: 12px;
    width: 262px; height: 262px; border-radius: 50%;
    background: var(--navy-deep);
    border: 2px solid rgba(0, 0, 0, 0.15);
  }
  .holder {
    position: absolute; left: 38px; top: 58px;
    font-weight: 700; font-size: 15px; line-height: 18px;
  }
  .holder__name { color: var(--cyan); }
  .holder__role { color: var(--white); }
  .contacts {
    position: absolute; left: 38px; top: 140px;
    list-style: none; font-size: 16px; line-height: 18px;
  }
  .contacts li {
    display: flex; align-items: flex-start; gap: 10px; margin-bottom: 12px;
  }
  .contacts svg { flex: none; width: 22px; height: 20px; fill: var(--white); }
  .contacts .icon-mail { fill: none; stroke: var(--white); stroke-width: 1.6; }
</style>
</head>
<body>
<main class="stage">
  <section class="card card--front" aria-label="Card front">
    <span class="brand-dot" aria-hidden="true"></span>
    <h1 class="brand-name">Northmerrow Capital</h1>
    <p class="brand-url">www.northmerrowcap.com</p>
  </section>

  <section class="card card--back" aria-label="Card back">
    <span class="back-disc" aria-hidden="true"></span>
    <div class="holder">
      <p class="holder__name">Your Name lst name</p>
      <p class="holder__role">CEO</p>
    </div>
    <ul class="contacts">
      <li>
        <svg viewBox="0 0 22 20" aria-hidden="true"><path d="M11 1 L1 10 H4 V19 H9 V13 H13 V19 H18 V10 H21 Z"/></svg>
        <span>PO Box 2740 address, Marholt<br>Nordavia</span>
      </li>
      <li>
        <svg viewBox="0 0 22 20" aria-hidden="true"><path d="M2 6 C2 3 6 2 11 2 C16 2 20 3 20 6 V8 H15 V6 H7 V8 H2 Z M5 10 H17 L19 18 H3 Z"/></svg>
        <span>+11 5550148822</span>
      </li>
      <li>
        <svg class="icon-mail" viewBox="0 0 22 20" aria-hidden="true"><rect x="1.5" y="3.5" width="19" height="13"/><path d="M1.5 3.5 L11 11 L20.5 3.5 M1.5 16.5 L8.5 9 M20.5 16.5 L13.5 9"/></svg>
        <span>abc@northmerrowcap.com</span>
      </li>
    </ul>
  </section>
</main>
</body>
</html>
```